Consulting company needs website design

We need a simple, static website design for our consulting company. We are looking for a general design of the look and feel of the website. Initially, it will have these pages:
- Home
- About us
- Services
- Contact us
We have our own logo which I have attached to the brief.

We are looking for a simple website, with white background and the use of gray (darker) as the main theme. Simple fonts. The website should be responsive so it an be easily red in mobile devices.

As part of the project, we will need to receive at least the following items:
- Individual files with sample text to support the pages outlined above
- Necessary CSS files

Our current website is here: http://www.lantrovale.co/

Here are some examples of other website we like to be used as guideline:
- http://www.morvicaplanos.com/
-

Target Market(s)

Individuals and companies looking to hire our company to provide consulting services.

Industry/Entity Type

It Company

Coding

Coded - Design and coding required

Number of Pages Required

4 page

Font styles to use
Sans Serif

Requirements
Must have
• Main page should have the ability to embed Chirplet feed into it.
• We prefer the design to use gray tones.

```html
<!DOCTYPE html>
<html lang="en">
<head>
<meta charset="utf-8">
<title>Lantrovale Group SAS</title>
<link rel="stylesheet" href="https://fonts.googleapis.com/css2?family=Michroma&family=Lato:ital,wght@0,400;0,700;1,400&family=Oswald:wght@500&display=swap">
<style>
:root{
  --ink:#1a1a1a;
  --dark:#2f2f2f;
  --footer:#333333;
  --bottom:#1f1f1f;
  --grey:#6b6b6b;
  --mid:#8a8a8a;
  --light:#f4f4f4;
  --line:#cfcfcf;
  --white:#ffffff;
  --node:#a5a5a5;
}
*{margin:0;padding:0;box-sizing:border-box}
html,body{width:1200px;height:2273px;overflow:hidden;background:var(--white)}
body{font-family:'Lato',sans-serif;color:var(--ink);position:relative}
.page{position:relative;width:1200px;height:2273px;overflow:hidden}

/* header */
.site-header{position:absolute;top:0;left:0;width:1200px;height:94px;background:linear-gradient(#ffffff,#efefef)}
.brand{position:absolute;left:103px;top:14px;display:flex;align-items:center;gap:14px}
.brand-mark{width:64px;height:64px;border-radius:50%;background:#d9d9d9}
.brand-name{font-family:'Lato',sans-serif;font-weight:700;font-size:28px;line-height:32px;color:var(--ink);width:170px}
.contact-bar{position:absolute;top:12px;right:100px;display:flex;align-items:center;gap:10px;font-size:15px;color:var(--ink)}
.contact-icon{width:24px;height:24px;border-radius:50%;background:var(--grey);display:flex;align-items:center;justify-content:center}
.contact-bar .gap{width:14px}
.main-nav{position:absolute;top:61px;left:645px;display:flex;height:33px;align-items:center}
.main-nav a{font-family:'Lato',sans-serif;font-weight:700;font-size:13px;color:var(--ink);text-decoration:none;letter-spacing:.3px}
.main-nav .active{background:var(--ink);color:var(--white);width:72px;height:33px;display:flex;align-items:center;justify-content:center;margin-right:50px}
.main-nav .n2{margin-right:65px}
.main-nav .n3{margin-right:66px}

/* hero */
.hero{position:absolute;top:94px;left:0;width:1200px;height:512px}
.hero-image{position:absolute;inset:0;background:radial-gradient(ellipse at 50% 40%,#5c6670 0%,#303030 35%,#1d1d1d 100%)}
.hero-caption{position:absolute;left:103px;top:206px;background:rgba(0,0,0,.75);padding:6px 12px;font-family:'Oswald',sans-serif;font-weight:500;font-size:30px;line-height:40px;color:var(--white)}
.hero-rule{position:absolute;left:98px;top:310px;width:3px;height:98px;background:var(--white)}
.slide-arrow{position:absolute;top:242px;width:38px;height:30px;background:rgba(255,255,255,.8);display:flex;align-items:center;justify-content:center}
.slide-arrow.prev{left:0}
.slide-arrow.next{right:0}

/* about */
.about{position:absolute;top:606px;left:0;width:1200px;height:321px;text-align:center}
.section-title{font-family:'Michroma',sans-serif;font-size:33px;color:var(--ink)}
.about .section-title{position:absolute;top:36px;width:100%}
.title-rule{position:absolute;left:307px;width:586px;height:1px;background:var(--line)}
.title-rule::after{content:"";position:absolute;left:50%;margin-left:-57px;top:-2px;width:114px;height:4px;background:var(--ink)}
.about .title-rule{top:95px}
.about-text{position:absolute;top:118px;left:108px;width:984px;font-size:13.5px;line-height:25px;color:#333}
.btn-more{position:absolute;top:244px;left:536px;width:128px;height:37px;background:var(--grey);color:var(--white);font-size:15px;display:flex;align-items:center;justify-content:center;border:1px solid #555;text-decoration:none}

/* services */
.services{position:absolute;top:927px;left:0;width:1200px;height:714px}
.services-photo{position:absolute;inset:0;background:linear-gradient(100deg,#3c4147 0%,#565b61 40%,#4a4e53 70%,#2d3033 100%)}
.services-diagram{position:absolute;inset:0}
.svc-title{font-family:'Michroma',sans-serif;font-size:33px;fill:var(--white)}
.svc-label{font-family:'Lato',sans-serif;font-size:18px;fill:var(--white)}

/* feeds */
.feeds{position:absolute;top:1641px;left:0;width:1200px;height:306px;background:var(--light)}
.col-title{position:absolute;top:48px;font-family:'Michroma',sans-serif;font-size:29px;color:var(--ink)}
.col-rule{position:absolute;top:95px;height:2px;background:#bdbdbd}
.pager{position:absolute;top:58px;display:flex;gap:4px}
.pager span{width:17px;height:17px;border-radius:50%;border:1px solid #999}
.pager span:last-child{border-color:var(--ink)}
.tweet{position:absolute;left:100px;width:470px;display:flex;gap:10px}
.avatar{width:55px;height:55px;background:linear-gradient(#c89a78,#8a6a50);flex:none}
.tweet-name{font-weight:700;font-size:14px}
.tweet-time{font-style:italic;color:var(--mid);font-size:12px;margin-left:8px;font-weight:400}
.tweet-text{font-size:13px;line-height:20px;color:#555}
.tweet-text b{color:var(--ink)}
.tweet-divider{position:absolute;left:100px;top:184px;width:470px;height:1px;background:var(--line)}
.col-divider{position:absolute;left:630px;top:40px;width:1px;height:240px;background:var(--line)}
.client-photo{position:absolute;left:628px;top:116px;width:92px;height:92px;border-radius:50%;border:3px solid var(--ink);background:linear-gradient(#b79a86,#5a4a40)}
.client-name{position:absolute;left:625px;top:215px;font-size:14px;font-weight:700;color:var(--ink)}
.quote{position:absolute;left:744px;top:114px;width:358px;font-style:italic;font-size:14px;line-height:21px;color:#444}

/* footer */
.site-footer{position:absolute;top:1947px;left:0;width:1200px;height:277px;background:var(--footer);color:#ddd}
.f-col{position:absolute;top:48px}
.f-head{font-weight:700;font-size:16px;color:var(--white);padding-bottom:8px;border-bottom:1px solid #777;display:inline-block}
.f-links{list-style:none;margin-top:12px}
.f-links li{font-size:14px;line-height:31px}
.f-links li::before{content:"› ";}
.f-contact{margin-top:16px;font-size:12.5px;line-height:16px}
.f-row{display:flex;gap:12px;margin-bottom:12px;align-items:flex-start}
.f-row svg{flex:none}
.map{position:absolute;left:615px;top:95px;width:224px;height:132px;border:3px solid #eee;background:linear-gradient(135deg,#cfe0c8,#b7cbe0 60%,#d9d4b8)}
.social{display:flex;gap:11px;margin-top:18px}
.social span{width:30px;height:30px;border-radius:50%;border:2px solid #eee}
.footer-mark{position:absolute;left:982px;top:152px;width:72px;height:72px;border-radius:50%;background:#e6e6e6}
.copyright{position:absolute;top:2224px;left:0;width:1200px;height:49px;background:var(--bottom);color:#e6e6e6;font-size:13px;display:flex;align-items:center;justify-content:center}
</style>
</head>
<body>
<div class="page">

<header class="site-header">
  <div class="brand"><span class="brand-mark"></span><span class="brand-name">Lantrovale Group SAS</span></div>
  <div class="contact-bar">
    <span class="contact-icon"><svg width="12" height="9" viewBox="0 0 12 9"><rect x=".5" y=".5" width="11" height="8" fill="none" stroke="#fff"/><path d="M.5 .5 6 5l5.5-4.5" fill="none" stroke="#fff"/></svg></span>
    <span>info@lantrovalegroupsas.com</span>
    <span class="gap"></span>
    <span class="contact-icon"><svg width="12" height="12" viewBox="0 0 12 12"><path d="M2 1l2 0 1 3-1.5 1a7 7 0 0 0 3.5 3.5L8 7l3 1v2a1 1 0 0 1-1 1A9 9 0 0 1 1 2a1 1 0 0 1 1-1z" fill="#fff"/></svg></span>
    <span>+ (123) 456 7890</span>
  </div>
  <nav class="main-nav">
    <a class="active" href="#">HOME</a>
    <a class="n2" href="#">ABOUT US</a>
    <a class="n3" href="#">SERVICES</a>
    <a href="#">CONTACT US</a>
  </nav>
</header>

<section class="hero">
  <div class="hero-image" role="img" aria-label="Chalkboard covered in hand-drawn business charts around a keyhole opening onto a city skyline"></div>
  <div class="hero-caption">We Specialise In Helping<br>Our Clients Succeed</div>
  <div class="hero-rule"></div>
  <div class="slide-arrow prev"><svg width="10" height="14" viewBox="0 0 10 14"><path d="M8 1 2 7l6 6" fill="none" stroke="#333" stroke-width="3"/></svg></div>
  <div class="slide-arrow next"><svg width="10" height="14" viewBox="0 0 10 14"><path d="M2 1l6 6-6 6" fill="none" stroke="#333" stroke-width="3"/></svg></div>
</section>

<section class="about">
  <h2 class="section-title">About Lantrovale Group SAS</h2>
  <div class="title-rule"></div>
  <p class="about-text">Lorem ipsum dolor sit amet, consectetuer adipiscing elit, sed diam nonummy nibh euismod tincidunt ut laoreet dolore magna aliquam erat volutpat. Ut wisi enim ad minim veniam, quis nostrud exerci tation ullamcorper suscipit lobortis nisl ut aliquip ex ea commodo consequat. Duis autem vel eum iriure dolor in hendrerit in vulputate velit esse molestie consequat, vel illum dolore eu feugiat nulla facilisis at vero eros et accumsan et iusto odio dignissim qui blandit praesent luptatum zzril delenit augue duis dolore te feugait nulla facilisi nonummy nibh euismod tincidunt ut laoreet dolore magna aliquam erat volutpat.</p>
  <a class="btn-more" href="#">Read More &raquo;</a>
</section>

<section class="services">
  <div class="services-photo" role="img" aria-label="Blurred photo of a team working over charts at a desk"></div>
  <svg class="services-diagram" width="1200" height="714" viewBox="0 0 1200 714">
    <text class="svc-title" x="600" y="72" text-anchor="middle">Services We Offere</text>
    <line x1="333" y1="95" x2="867" y2="95" stroke="#999" stroke-width="1"/>
    <rect x="553" y="93" width="94" height="4" fill="#111"/>
    <circle cx="600" cy="403" r="225" fill="none" stroke="#d8d8d8" stroke-width="7"/>
    <circle cx="600" cy="403" r="72" fill="#f2f2f2"/>
    <g stroke="#bbb" stroke-width="1" fill="none">
      <path d="M385 171h45l28 22"/><path d="M740 171h-30l-18 22"/>
      <path d="M296 320h50"/><path d="M904 320h-50"/>
      <path d="M281 482h50"/><path d="M919 482h-50"/>
      <path d="M341 637h60l20-26"/><path d="M860 637h-60l-20-26"/>
    </g>
    <g fill="#fff">
      <circle cx="385" cy="171" r="3"/><circle cx="815" cy="171" r="3"/>
      <circle cx="296" cy="320" r="3"/><circle cx="904" cy="320" r="3"/>
      <circle cx="281" cy="482" r="3"/><circle cx="919" cy="482" r="3"/>
      <circle cx="341" cy="637" r="3"/><circle cx="860" cy="637" r="3"/>
    </g>
    <g stroke="#fff" stroke-width="6" fill="#a5a5a5">
      <circle cx="505" cy="197" r="47"/><circle cx="694" cy="197" r="47"/>
      <circle cx="394" cy="320" r="47"/><circle cx="806" cy="320" r="47"/>
      <circle cx="377" cy="482" r="47"/><circle cx="823" cy="482" r="47"/>
      <circle cx="465" cy="611" r="47" fill="#111"/><circle cx="733" cy="611" r="47"/>
    </g>
    <g fill="#111">
      <circle cx="505" cy="197" r="16"/><circle cx="505" cy="197" r="7" fill="#a5a5a5"/>
      <rect x="674" y="184" width="40" height="28" rx="3"/><rect x="686" y="178" width="16" height="8" fill="none" stroke="#111" stroke-width="3"/>
      <rect x="378" y="316" width="8" height="20"/><rect x="390" y="306" width="8" height="30"/><circle cx="410" cy="328" r="7" fill="none" stroke="#111" stroke-width="3"/>
      <path d="M786 318l14-10 12 8 14-8v14l-14 12-12-4-14-4z"/>
      <path d="M360 470l34 24M394 470l-34 24" stroke="#111" stroke-width="3"/>
      <rect x="807" y="470" width="4" height="26"/><rect x="815" y="478" width="4" height="18"/><rect x="823" y="474" width="4" height="22"/><circle cx="834" cy="484" r="8" fill="none" stroke="#111" stroke-width="3"/>
      <circle cx="465" cy="611" r="20" fill="none" stroke="#fff" stroke-width="3"/><path d="M445 611h40M465 591v40" stroke="#fff" stroke-width="2"/>
      <path d="M712 596h30v18h-22l-8 6z"/><path d="M728 604h24v18l-6-4h-18z"/>
    </g>
    <g class="svc-label">
      <text x="371" y="176" text-anchor="end">Brand</text><text x="371" y="202" text-anchor="end">Development</text>
      <text x="830" y="176">Corporate Finance</text><text x="830" y="202">&amp; Restructuring</text>
      <text x="282" y="324" text-anchor="end">Market</text><text x="282" y="350" text-anchor="end">Research</text>
      <text x="917" y="324">Mergers</text><text x="917" y="350">&amp; Acquisitions</text>
      <text x="267" y="486" text-anchor="end">Market Entry</text><text x="267" y="512" text-anchor="end">Strategy</text>
      <text x="933" y="486">Corporate Finance</text><text x="933" y="512">&amp; Restructuring</text>
      <text x="327" y="641" text-anchor="end">Overseas Marketing</text><text x="327" y="667" text-anchor="end">&amp; Promotion</text>
      <text x="873" y="641">Strategic</text><text x="873" y="667">Communications</text>
    </g>
  </svg>
</section>

<section class="feeds">
  <h3 class="col-title" style="left:98px">Chirplet Feeds</h3>
  <div class="pager" style="left:529px"><span></span><span></span></div>
  <div class="col-rule" style="left:98px;width:472px"></div>
  <div class="tweet" style="top:116px">
    <div class="avatar" role="img" aria-label="Author portrait"></div>
    <div><div class="tweet-name">Maya Collins<span class="tweet-time">3 minutes ago</span></div>
    <div class="tweet-text">Lorem ipsum dolor sit amet, consectetuer nonu mmy nibh euismod ipsum dolor tincidunt utla <b>http://adipiscin elit sed diam</b></div></div>
  </div>
  <div class="tweet-divider"></div>
  <div class="tweet" style="top:198px">
    <div class="avatar" role="img" aria-label="Author portrait"></div>
    <div><div class="tweet-name">Maya Collins<span class="tweet-time">3 minutes ago</span></div>
    <div class="tweet-text">Lorem ipsum dolor sit amet, consectetuer nonu mmy nibh euismod ipsum dolor tincidunt utla <b>http://adipiscin elit sed diam</b></div></div>
  </div>
  <div class="col-divider"></div>
  <h3 class="col-title" style="left:630px">Clients Testimonials</h3>
  <div class="pager" style="left:1061px"><span></span><span></span></div>
  <div class="col-rule" style="left:630px;width:472px"></div>
  <div class="client-photo" role="img" aria-label="Client portrait"></div>
  <div class="client-name">- Peter Anselm</div>
  <p class="quote">&ldquo; Lorem ipsumn sit amet co adipisclitsed udml eisli mol monk dtepor incidiunt ut la dolore ma aliquanmi kn nibhmi enim nim veni exercitation ullamco ips sdlitnol am conoplk adipiscig elitsedmi do eiusmod te epo uom acculi dollarmjk oremque laudantium. Accusant doloremquen more consec moptnonumyl facilest. &rdquo;</p>
</section>

<footer class="site-footer">
  <div class="f-col" style="left:100px">
    <span class="f-head">Quick Links</span>
    <ul class="f-links"><li>Home</li><li>About Us</li><li>Services</li><li>Contact</li></ul>
  </div>
  <div class="f-col" style="left:305px;width:200px">
    <span class="f-head" style="width:200px">Contact Details</span>
    <div class="f-contact">
      <div class="f-row"><svg width="14" height="20" viewBox="0 0 14 20"><path d="M7 0a7 7 0 0 1 7 7c0 5-7 13-7 13S0 12 0 7a7 7 0 0 1 7-7z" fill="#ddd"/><circle cx="7" cy="7" r="3" fill="#333"/></svg><div><b>Lantrovale Group SAS</b><br>123 PG Duis Aute Irur Dolore<br>Srephenderit Amit In Voluptate</div></div>
      <div class="f-row"><svg width="14" height="14" viewBox="0 0 12 12"><path d="M2 1l2 0 1 3-1.5 1a7 7 0 0 0 3.5 3.5L8 7l3 1v2a1 1 0 0 1-1 1A9 9 0 0 1 1 2a1 1 0 0 1 1-1z" fill="#ddd"/></svg><div>+ (123) 456 7890</div></div>
      <div class="f-row"><svg width="14" height="14" viewBox="0 0 14 14"><rect x="3" y="0" width="8" height="4" fill="#ddd"/><rect x="0" y="5" width="14" height="6" fill="#ddd"/><rect x="3" y="9" width="8" height="5" fill="#ddd"/></svg><div>+ (123) 456 7890</div></div>
      <div class="f-row"><svg width="14" height="10" viewBox="0 0 12 9"><rect x=".5" y=".5" width="11" height="8" fill="none" stroke="#ddd"/><path d="M.5 .5 6 5l5.5-4.5" fill="none" stroke="#ddd"/></svg><div>info@lantrovalegroupsas.com</div></div>
    </div>
  </div>
  <div class="f-col" style="left:615px"><span class="f-head" style="width:224px">Location Map</span></div>
  <div class="map" role="img" aria-label="Street map showing the office location"></div>
  <div class="f-col" style="left:942px">
    <span class="f-head" style="width:158px">Follow Us</span>
    <div class="social"><span></span><span></span><span></span><span></span></div>
  </div>
  <div class="footer-mark"></div>
</footer>
<div class="copyright">Copyright &copy; 2016 Lantrovale Group SAS.&nbsp; All Rights Reserved.</div>

</div>
</body>
</html>
```